Teach English Abroad Landing Page Design

This is a really important page to us and we want it to show in the design. We're creating a design for the pillar page called teach English abroad. Here is a design brief for the page - https://files.plovarix.net/doc/8QwTn3Lk5ZpVb2RmXc7YdHs-_fJ4aGe9UoNiKt1WqEzr/edit?usp=sharing

```html
<!DOCTYPE html>
<html lang="en">
<head>
<meta charset="utf-8">
<title>Teach English Abroad – Lingoway Academy</title>
<link href="https://fonts.googleapis.com/css2?family=Poppins:ital,wght@0,400;0,500;0,600;0,700;1,500;1,600&family=Dancing+Script:wght@600&display=swap" rel="stylesheet">
<style>
:root{
  --teal:#17b3bd;
  --teal-dark:#0f8f98;
  --orange:#f5a43a;
  --ink:#222;
  --text:#555;
  --muted:#777;
  --panel:#f4f4f4;
  --band:#e3f4f5;
  --line:#d8d8d8;
}
*{margin:0;padding:0;box-sizing:border-box}
html,body{width:717px;height:1200px;overflow:hidden;background:#fff}
body{position:relative;font-family:'Poppins',sans-serif;color:var(--ink)}
.abs{position:absolute}

/* header */
.brand{left:40px;top:14px;display:flex;align-items:center;gap:6px;font-size:11px;font-weight:600;color:var(--teal)}
.brand-mark{width:16px;height:16px;background:var(--teal)}
.search{left:510px;top:12px;width:112px;height:18px;border:1px solid #aaa;font-size:6px;color:#666;display:flex;justify-content:space-between;align-items:center;padding:0 6px}
.cta-small{left:625px;top:12px;width:55px;height:18px;background:var(--teal);color:#fff;font-size:5.6px;font-weight:500;display:flex;align-items:center;justify-content:center}
.nav{top:40px;font-size:8px;color:#333}
.nav.active{color:var(--teal)}

/* hero */
.hero{left:0;top:64px;width:717px;height:320px;background:linear-gradient(90deg,#3a3f3c 0%,#244845 30%,#2c4b48 60%,#3d4240 100%)}
.hero-title{top:182px;width:717px;text-align:center;color:#fff;font-size:29px;font-weight:700}
.hero-script{top:230px;width:717px;text-align:center;color:#fff;font-family:'Dancing Script',cursive;font-size:22px}
.hero-btn{left:318px;top:290px;width:83px;height:27px;background:var(--teal);color:#fff;font-size:7.5px;font-weight:500;display:flex;align-items:center;justify-content:center}

/* breadcrumb */
.crumbs{left:26px;top:409px;font-size:8px;color:#333;display:flex;gap:12px}
.crumbs .here{color:var(--teal)}
.share{top:409px;width:16px;height:16px;border-radius:50%}

/* sidebar */
.sidebar{left:0;top:445px;width:217px;height:755px;background:var(--panel)}
.outline-title{left:16px;top:475px;border-left:3px solid var(--teal);padding-left:6px;font-size:12px;font-weight:500;line-height:15px}
.sub-box{left:16px;top:607px;width:185px;height:377px;background:#fff}
.band{left:16px;top:585px;width:185px;height:23px;background:var(--band)}
.item{left:26px;font-size:8px;color:#333;white-space:nowrap;line-height:10px}
.item.active{color:var(--teal)}
.sub{left:36px;font-size:6.8px;color:#333;white-space:nowrap;line-height:9px}
.subsub{left:46px;font-size:6.5px;color:#444;line-height:9px}
.caret{left:182px;width:0;height:0;border-left:3px solid transparent;border-right:3px solid transparent}
.caret.down{border-top:3.5px solid #333}
.caret.up{border-bottom:3.5px solid #333}
.caret.teal{border-top-color:var(--teal)}

/* main */
.main-title{left:257px;top:462px;font-size:20px;font-weight:700;color:var(--teal)}
.lede{left:257px;top:507px;width:425px;font-size:8.1px;line-height:12px;color:var(--text)}
.lede b{color:#222;font-weight:600}
.req{top:562px;display:flex;align-items:center;gap:6px;font-size:7.3px;line-height:10.5px;color:#444}
.req svg{width:20px;height:20px;stroke:#333;fill:none;stroke-width:1.2}

.stat-accent{left:257px;top:634px;width:4px;height:180px;background:var(--orange)}
.stat-box{left:271px;top:634px;width:411px;height:180px;background:var(--panel)}
.stat-text{left:457px;top:668px;width:200px;font-size:8.3px;line-height:17px;color:#444}
.stat-text a{color:var(--teal);text-decoration:none}
.stat-text b{color:#222;font-weight:600}

.banner{left:257px;top:854px;width:425px;height:78px;background:linear-gradient(180deg,#2f8aa0 0%,#1c7e93 60%,#2a91a3 100%);color:#fff;font-style:italic;font-size:10.8px;font-weight:500;line-height:19px;padding:20px 30px 0 31px}
.banner strong{font-size:15px;font-weight:600}

.para{left:257px;width:425px;font-size:8.1px;line-height:12px;color:var(--text)}

.acc-head{left:255px;top:1075px;width:423px;height:30px;border-left:4px solid var(--teal);border-bottom:1px solid var(--line);font-size:11.5px;font-weight:600;padding:7px 0 0 10px}
.acc-body{left:255px;top:1105px;width:423px;height:95px;background:var(--panel)}
.acc-text{left:275px;top:1135px;width:390px;font-size:8.1px;line-height:12px;color:#333}
.acc-list{left:308px;top:1179px;width:330px;font-size:8.1px;line-height:12px;color:#444}
</style>
</head>
<body>

<header>
  <div class="abs brand"><span class="brand-mark"></span>Lingoway Academy</div>
  <div class="abs search"><span>Search</span><span>Go›</span></div>
  <div class="abs cta-small">EXPLORE NOW</div>
  <span class="abs nav" style="left:443px">Home</span>
  <span class="abs nav" style="left:488px">Asia</span>
  <span class="abs nav active" style="left:524px">Teach English Abroad</span>
  <span class="abs nav" style="left:631px">South Korea</span>
</header>

<section>
  <div class="abs hero" role="img" aria-label="Photo of a smiling teacher with glasses leaning on a chair in front of a classroom chalkboard"></div>
  <h1 class="abs hero-title">Teach English Abroad</h1>
  <div class="abs hero-script">teach English abroad</div>
  <div class="abs hero-btn">EXPLORE NOW ›</div>
</section>

<nav class="abs crumbs"><span>Home</span><span>›</span><span>Asia</span><span>›</span><span class="here">Teach English Abroad</span></nav>
<span class="abs share" style="left:625px;background:#3b5998"></span>
<span class="abs share" style="left:644px;background:#1da1f2"></span>
<span class="abs share" style="left:663px;background:#cb2027"></span>

<aside>
  <div class="abs sidebar"></div>
  <h2 class="abs outline-title">Content Outline</h2>
  <div class="abs band"></div>
  <div class="abs sub-box"></div>

  <span class="abs item active" style="top:516px">Teach English abroad</span><i class="abs caret down teal" style="top:519px"></i>
  <span class="abs item" style="top:541px">Why teach English abroad?</span><i class="abs caret down" style="top:544px"></i>
  <span class="abs item" style="top:566px">Where to teach English abroad?</span><i class="abs caret down" style="top:569px"></i>
  <span class="abs item" style="top:592px">Requirements and qualifications</span><i class="abs caret up" style="top:594px"></i>

  <span class="abs sub" style="top:616px">What are the basic requirements for te...</span><i class="abs caret up" style="top:618px"></i>
  <span class="abs subsub" style="top:632px">Be fluent in English</span>
  <span class="abs subsub" style="top:647px">Get TEFL certified</span>
  <span class="abs subsub" style="top:662px">Bachelor's degree</span>
  <span class="abs sub" style="top:679px">Do you need a visa to teach English ab...</span><i class="abs caret up" style="top:681px"></i>
  <span class="abs subsub" style="top:695px">Asia</span>
  <span class="abs subsub" style="top:710px">Europe</span>
  <span class="abs subsub" style="top:725px">South America</span>
  <span class="abs subsub" style="top:740px">Middle East</span>
  <span class="abs sub" style="top:757px">Do I need teaching experience to teach...</span><i class="abs caret up" style="top:759px"></i>
  <span class="abs subsub" style="top:773px">Volunteer teaching</span>
  <span class="abs subsub" style="top:788px">Combined TEFL Course</span>
  <span class="abs subsub" style="top:803px">Internship programmes</span>
  <span class="abs sub" style="top:820px">Which TEFL certification is best for teach...</span><i class="abs caret up" style="top:822px"></i>
  <span class="abs subsub" style="top:836px">Level 3 - 120 hours</span>
  <span class="abs subsub" style="top:851px">Level 5 - 168 hours</span>
  <span class="abs subsub" style="top:866px">Combined Level 5 - 168 hours</span>
  <span class="abs sub" style="top:883px">Can I teach abroad without a degree?</span><i class="abs caret down" style="top:886px"></i>
  <span class="abs sub" style="top:903px">Can I teach English as a non-native sp...</span><i class="abs caret down" style="top:906px"></i>
  <span class="abs sub" style="top:923px">Do I need to purchase my own healthc...</span><i class="abs caret down" style="top:926px"></i>
  <span class="abs sub" style="top:943px">Do I need to get travel insurance?</span><i class="abs caret down" style="top:946px"></i>
  <span class="abs sub" style="top:963px">How much startup capital do I need to...</span><i class="abs caret down" style="top:966px"></i>

  <span class="abs item" style="top:993px">Jobs and Programs</span><i class="abs caret down" style="top:996px"></i>
  <span class="abs item" style="top:1018px">Salaries and Benefits</span><i class="abs caret down" style="top:1021px"></i>
  <span class="abs item" style="top:1043px">Where will you teach abroad in 2023?</span><i class="abs caret down" style="top:1046px"></i>
  <span class="abs item" style="top:1069px">Teach Abroad By Country</span><i class="abs caret down" style="top:1072px"></i>
  <span class="abs item" style="top:1094px">Teach Abroad By Popular Cities</span><i class="abs caret down" style="top:1097px"></i>
</aside>

<main>
  <h2 class="abs main-title">Teach English Abroad</h2>
  <p class="abs lede">Teaching English abroad involves travelling and living in a foreign country while teaching English as a foreign language to non-native speakers. Teaching English this way is not just reserved for teachers but <b>anyone that meets the following requirements can qualify</b>.</p>

  <div class="abs req" style="left:267px">
    <svg viewBox="0 0 20 20"><rect x="4" y="2" width="12" height="16" rx="1"/><circle cx="10" cy="9" r="4"/><path d="M6 9h8M10 5v8M7 15h6"/></svg>
    <span>Valid passport/<br>visa</span></div>
  <div class="abs req" style="left:367px">
    <svg viewBox="0 0 20 20"><path d="M4 16v-4a6 6 0 1 1 10-3l1 3h-2v3h-3v2"/><path d="M15 8l3-1M15 11h3"/></svg>
    <span>Fluent in English</span></div>
  <div class="abs req" style="left:470px">
    <svg viewBox="0 0 20 20"><path d="M5 3h10l-1 3H6z"/><circle cx="10" cy="9" r="3"/><path d="M3 18c0-4 3-6 7-6s7 2 7 6z"/></svg>
    <span>Bachelor’s degree<br>(for some countries)</span></div>
  <div class="abs req" style="left:590px">
    <svg viewBox="0 0 20 20"><rect x="2" y="3" width="13" height="15"/><path d="M5 7h7M5 10h7M5 13h4"/><circle cx="15" cy="13" r="3"/></svg>
    <span>TEFL certificate</span></div>

  <div class="abs stat-accent"></div>
  <div class="abs stat-box"></div>
  <svg class="abs" style="left:290px;top:645px" width="140" height="150" viewBox="0 0 280 300" font-family="Poppins, sans-serif">
    <text x="30" y="16" font-size="5.2" font-weight="600" fill="#222">The most spoken languages worldwide in 2022 (by speakers in millions)</text>
    <g stroke="#e5e5e5" stroke-width="0.6">
      <line x1="54" y1="28" x2="54" y2="262"/><line x1="79.6" y1="28" x2="79.6" y2="262"/><line x1="105" y1="28" x2="105" y2="262"/><line x1="130.7" y1="28" x2="130.7" y2="262"/><line x1="156" y1="28" x2="156" y2="262"/><line x1="182" y1="28" x2="182" y2="262"/><line x1="207" y1="28" x2="207" y2="262"/><line x1="233" y1="28" x2="233" y2="262"/><line x1="258" y1="28" x2="258" y2="262"/>
    </g>
    <g fill="#2f6fde">
      <rect x="54" y="32" width="186" height="9"/><rect x="54" y="47.5" width="145" height="9"/><rect x="54" y="63" width="78" height="9"/><rect x="54" y="78.5" width="71" height="9"/><rect x="54" y="94" width="35" height="9"/><rect x="54" y="109.5" width="35" height="9"/><rect x="54" y="125" width="34.9" height="9"/><rect x="54" y="140.5" width="33" height="9"/><rect x="54" y="156" width="32.9" height="9"/><rect x="54" y="171.5" width="29.6" height="9"/><rect x="54" y="187" width="25.4" height="9"/><rect x="54" y="202.5" width="17.2" height="9"/><rect x="54" y="218" width="16" height="9"/><rect x="54" y="233.5" width="15.4" height="9"/><rect x="54" y="249" width="12.7" height="9"/>
    </g>
    <g font-size="4" fill="#666" text-anchor="end">
      <text x="50" y="38">English</text><text x="50" y="53.5">Chinese (Mandarin)</text><text x="50" y="69">Hindi</text><text x="50" y="84.5">Spanish</text><text x="50" y="100">French</text><text x="50" y="115.5">Arabic (standard)</text><text x="50" y="131">Bengali</text><text x="50" y="146.5">Russian</text><text x="50" y="162">Portuguese</text><text x="50" y="177.5">Urdu</text><text x="50" y="193">Indonesian</text><text x="50" y="208.5">German (standard)</text><text x="50" y="224">Japanese</text><text x="50" y="239.5">Nigerian Pidgin</text><text x="50" y="255">Marathi</text>
    </g>
    <g font-size="3.6" fill="#444">
      <text x="243" y="38">1,456</text><text x="202" y="53.5">1,138</text><text x="135" y="69">609.2</text><text x="128" y="84.5">559.3</text><text x="92" y="100">274.1</text><text x="92" y="115.5">274</text><text x="92" y="131">272.8</text><text x="90" y="146.5">258.2</text><text x="90" y="162">257.7</text><text x="87" y="177.5">231.3</text><text x="83" y="193">199</text><text x="74" y="208.5">134.6</text><text x="73" y="224">125.4</text><text x="72" y="239.5">120.7</text><text x="70" y="255">99.1</text>
    </g>
    <text x="156" y="276" font-size="3.6" fill="#666" text-anchor="middle">Speakers in millions</text>
    <text x="10" y="286" font-size="3.6" fill="#444">Source: survey data 2022</text>
    <text x="95" y="286" font-size="3.6" fill="#444">Additional information: worldwide estimates</text>
  </svg>
  <p class="abs stat-text"><a href="#">According to Datavista</a>, English is the most widely spoken language in the world - spoken by 1.5 billion people. As many speakers as there are, there are just as many, if not more, learners - <b>1 in every 4 people in the world are currently learning English.</b></p>

  <div class="abs banner" role="img" aria-label="Teal-tinted city skyline behind a statistic"><strong>20%</strong> of the Earth’s population are English language learners. English is the most spoken language in the world (1.5 billion people)</div>

  <p class="abs para" style="top:972px">Opportunities to teach English abroad is an exciting way to combine your love of travel with your passion for education while making a positive impact on the lives of others.</p>
  <p class="abs para" style="top:1011px">In this beginner's guide to teaching English abroad, we'll look at everything you need to know, including how to get started on this journey!</p>

  <h3 class="abs acc-head">Why teach English abroad?</h3>
  <i class="abs caret up" style="left:667px;top:1086px;border-left-width:4px;border-right-width:4px;border-bottom-width:5px"></i>
  <div class="abs acc-body"></div>
  <p class="abs acc-text">The fact that you’re here means this question is already on your mind. Now, allow us to answer your question with a couple of questions of ours:</p>
  <p class="abs acc-list">1. Would you like a fresh start and the chance to challenge yourself in new and exciting ways to get out of your comfort zone?</p>
</main>

</body>
</html>
```